QOR Exterior Coatings

double sided. the front i want the name of the business each word on a new line with the QOR being bigger. id like teal, black and white colors. the back i want my contact info. Flat, no gloss. Something professional and I want to feel the letters bump put of the card. if possible maybe a paint sprayer in corner. not a car paint spray. (no tank on top of gun)
no vehicle paint sprayers. that means no tank on top of the gun. doesn't have to have a sprayer. black/dark background on the front. white back ground on back with info

```html
<!DOCTYPE html>
<html lang="en">
<head>
<meta charset="utf-8">
<title>QOR Exterior Coatings – Business Card</title>
<link rel="stylesheet" href="https://fonts.googleapis.com/css2?family=Archivo+Black&family=Roboto:wght@400&display=swap">
<style>
  :root {
    --backdrop: #6e6e6e;
    --paper: #ffffff;
    --teal: #088582;
    --teal-deep: #054a52;
    --brand-dark: #0d4c55;
    --charcoal: #2a2b2b;
  }
  html, body {
    margin: 0;
    padding: 0;
    width: 1200px;
    height: 801px;
    overflow: hidden;
    background: var(--backdrop);
  }
  .sheet { display: block; width: 1200px; height: 801px; }
  .display { font-family: "Archivo Black", "Arial Black", sans-serif; }
  .body-text { font-family: "Roboto", Arial, sans-serif; }
  .brand-front { fill: var(--brand-dark); }
  .brand-back { fill: var(--paper); }
  .name-plate { fill: var(--charcoal); }
  .contact-band { fill: var(--teal); }
  .light-text { fill: var(--paper); }
  .icon { fill: none; stroke: var(--paper); stroke-width: 1.2; }
</style>
</head>
<body>
<svg class="sheet" viewBox="0 0 1200 801" xmlns="http://www.w3.org/2000/svg">
  <defs>
    <linearGradient id="back-gradient" x1="0" y1="1" x2="1" y2="0">
      <stop offset="0" stop-color="var(--teal-deep)"/>
      <stop offset="0.25" stop-color="var(--teal-deep)"/>
      <stop offset="0.5" stop-color="var(--teal)"/>
      <stop offset="0.72" stop-color="#066a6b"/>
      <stop offset="1" stop-color="var(--teal-deep)"/>
    </linearGradient>
  </defs>

  <!-- Contact side -->
  <g class="card card-contact" transform="translate(153 274)">
    <rect class="card-paper" width="443" height="263" fill="var(--paper)"/>
    <rect class="contact-band" y="156" width="443" height="107"/>
    <polygon class="name-plate" points="0,124 193,124 223,178 0,178"/>

    <g class="brand-lockup display brand-front">
      <text x="236" y="77" font-size="58" textLength="172" lengthAdjust="spacingAndGlyphs">QOR</text>
      <text x="236" y="102" font-size="23" textLength="170" lengthAdjust="spacingAndGlyphs">EXTERIOR</text>
      <text x="236" y="124" font-size="23" textLength="168" lengthAdjust="spacingAndGlyphs">COATINGS</text>
    </g>

    <text class="display light-text" x="28" y="157" font-size="16.5">DANIEL REEVE</text>
    <text class="body-text light-text" x="28" y="171" font-size="12.5">Managing Director</text>

    <g class="contact-list body-text light-text" font-size="12.5">
      <path class="icon" d="M31 201 q-2 0 -2 2 q1 6 7 8 q2 0 2 -2 l-2 -2 l-2 1 q-2 -1 -3 -3 l1 -2 z"/>
      <text x="45" y="209">044-310 552 764</text>
      <rect class="icon" x="29" y="218" width="12" height="8"/>
      <path class="icon" d="M29 218 l6 5 l6 -5"/>
      <text x="45" y="226">hello@qorcoatings.net</text>
      <circle class="icon" cx="35" cy="238" r="6"/>
      <ellipse class="icon" cx="35" cy="238" rx="2.6" ry="6"/>
      <path class="icon" d="M29 238 h12 M30 235 h10 M30 241 h10"/>
      <text x="45" y="242">www.qorcoatings.net</text>
    </g>

    <g class="address body-text light-text" font-size="12.5">
      <text x="281" y="225">87, Harbour View Road</text>
      <text x="281" y="241">Eastport, 31208</text>
    </g>
  </g>

  <!-- Brand side -->
  <g class="card card-brand" transform="translate(625 274)">
    <rect width="443" height="263" fill="url(#back-gradient)"/>
    <g class="brand-lockup display brand-back">
      <text x="108" y="128" font-size="76" textLength="227" lengthAdjust="spacingAndGlyphs">QOR</text>
      <text x="110" y="162" font-size="30" textLength="222" lengthAdjust="spacingAndGlyphs">EXTERIOR</text>
      <text x="110" y="190" font-size="30" textLength="218" lengthAdjust="spacingAndGlyphs">COATINGS</text>
    </g>
  </g>
</svg>
</body>
</html>
```